Kiosk Coin Venture: Safe and Secure Cash Money

Front of card: LOGO

Back of card:
$$$ FREE ATM PLACEMENT $$$
BENIFITS OF HAVING AN ATM AT YOUR BUSINESS
FREE ATM and BTM (Bitcoin) installation, maintenance, and loading.
Lower card processing fees
Stimulate more traffic.
Ease of access for customers
Maintain customers inside location.
Higher tips and spending

Contact me for more information!
Name: Tobias Merlano
Phone: (512) 638-9071 - Call or Text
Email: Tobias@KioskCoin.example

Contact Information for Business Card

The card should be shape of the logo. Only the back will have all the contact and business details.

Requirements
Must have
• The logo itself will be one side, the card will be the shape of the logo. contact details on back side.

```html
<!DOCTYPE html>
<html lang="en">
<head>
<meta charset="utf-8">
<title>Kiosk Coin Venture – Business Card</title>
<link rel="stylesheet" href="https://fonts.googleapis.com/css2?family=Barlow:wght@400;600;700&family=Barlow+Condensed:wght@700;800&display=swap">
<style>
  :root {
    --page-bg: #1c1c1d;
    --card-black: #0f0f10;
    --silver-light: #f2f2f2;
    --silver-mid: #bdbdbd;
    --silver-dark: #7a7a7a;
    --gold: #e3b82a;
    --gold-deep: #b8901a;
    --text-white: #f4f4f4;
    --text-grey: #a9a9a9;
  }
  * { box-sizing: border-box; margin: 0; padding: 0; }
  html, body {
    width: 1200px;
    height: 1122px;
    overflow: hidden;
    background: var(--page-bg);
  }
  .sheet {
    position: relative;
    width: 1200px;
    height: 1122px;
  }
  .card {
    position: absolute;
    top: 190px;
    width: 500px;
    height: 740px;
  }
  .card--front { left: 70px; }
  .card--back { left: 630px; }
  .card__shape {
    position: absolute;
    inset: 0;
    width: 500px;
    height: 740px;
  }
  .card__content {
    position: absolute;
    inset: 0;
    text-align: center;
    color: var(--text-white);
    font-family: "Barlow", sans-serif;
  }

  /* Front */
  .front-brand {
    position: absolute;
    left: 0;
    right: 0;
    top: 260px;
    display: flex;
    flex-direction: column;
    align-items: center;
    gap: 22px;
  }
  .front-brand__dot {
    width: 56px;
    height: 56px;
    border-radius: 50%;
    background: var(--gold);
  }
  .front-brand__name {
    font-family: "Barlow Condensed", sans-serif;
    font-weight: 800;
    font-size: 64px;
    line-height: 0.95;
    letter-spacing: 2px;
    text-transform: uppercase;
    color: var(--silver-mid);
  }

  /* Back */
  .back-headline {
    position: absolute;
    left: 0; right: 0;
    top: 138px;
    font-family: "Barlow Condensed", sans-serif;
    font-weight: 800;
    font-size: 34px;
    letter-spacing: 1px;
    color: var(--silver-mid);
  }
  .back-subline {
    position: absolute;
    left: 0; right: 0;
    top: 180px;
    font-weight: 700;
    font-size: 15.5px;
    letter-spacing: 0.5px;
    text-transform: uppercase;
    color: var(--text-grey);
  }
  .back-rule {
    position: absolute;
    left: 228px;
    top: 222px;
    width: 44px;
    height: 3px;
    background: var(--gold);
  }
  .benefits {
    position: absolute;
    left: 40px; right: 40px;
    top: 238px;
    list-style: none;
    font-size: 21px;
    line-height: 27px;
  }
  .benefits__lead { font-weight: 700; }
  .contact-name {
    position: absolute;
    left: 0; right: 0;
    top: 440px;
    font-family: "Barlow Condensed", sans-serif;
    font-weight: 800;
    font-size: 44px;
    letter-spacing: 1px;
    color: var(--silver-mid);
  }
  .contact-icons {
    position: absolute;
    left: 0; right: 0;
    top: 502px;
    display: flex;
    justify-content: center;
    gap: 10px;
  }
  .contact-icon {
    width: 32px;
    height: 32px;
  }
  .contact-phone {
    position: absolute;
    left: 0; right: 0;
    top: 540px;
    font-weight: 700;
    font-size: 34px;
  }
  .contact-email {
    position: absolute;
    left: 0; right: 0;
    top: 588px;
    font-size: 22px;
  }
</style>
</head>
<body>
<main class="sheet">

  <svg width="0" height="0" style="position:absolute" aria-hidden="true">
    <defs>
      <linearGradient id="silver-sheen" x1="0" y1="0" x2="1" y2="1">
        <stop offset="0" stop-color="#f4f4f4"/>
        <stop offset="0.45" stop-color="#9a9a9a"/>
        <stop offset="0.7" stop-color="#e8e8e8"/>
        <stop offset="1" stop-color="#7d7d7d"/>
      </linearGradient>
      <linearGradient id="silver-band" x1="0" y1="0" x2="1" y2="0">
        <stop offset="0" stop-color="#8a8a8a"/>
        <stop offset="0.35" stop-color="#f0f0f0"/>
        <stop offset="0.65" stop-color="#a5a5a5"/>
        <stop offset="1" stop-color="#ececec"/>
      </linearGradient>
    </defs>
  </svg>

  <!-- Front side -->
  <section class="card card--front" aria-label="Card front">
    <svg class="card__shape" viewBox="0 0 500 740" aria-hidden="true">
      <path d="M105,4 L395,4 L496,105 L496,500 Q496,580 430,630 L290,720 Q250,744 210,720 L70,630 Q4,580 4,500 L4,105 Z"
            fill="url(#silver-sheen)"/>
      <path d="M112,20 L388,20 L480,112 L480,496 Q480,570 420,616 L282,704 Q250,724 218,704 L80,616 Q20,570 20,496 L20,112 Z"
            fill="var(--card-black)"/>
    </svg>
    <div class="card__content">
      <div class="front-brand">
        <span class="front-brand__dot"></span>
        <p class="front-brand__name">Kiosk Coin<br>Venture</p>
      </div>
    </div>
  </section>

  <!-- Back side -->
  <section class="card card--back" aria-label="Card back">
    <svg class="card__shape" viewBox="0 0 500 740" aria-hidden="true">
      <path d="M105,4 L395,4 L496,105 L496,500 Q496,580 430,630 L290,720 Q250,744 210,720 L70,630 Q4,580 4,500 L4,105 Z"
            fill="url(#silver-sheen)"/>
      <path d="M112,12 L388,12 L488,112 L488,498 Q488,574 424,622 L286,712 Q250,732 214,712 L76,622 Q12,574 12,498 L12,112 Z"
            fill="var(--card-black)"/>
      <path d="M118,36 L382,36 L446,100 L446,122 L54,122 L54,100 Z" fill="url(#silver-band)"/>
    </svg>
    <div class="card__content">
      <h1 class="back-headline">$$$ FREE ATM PLACEMENT $$$</h1>
      <p class="back-subline">Benefits of having an ATM at your business</p>
      <span class="back-rule"></span>
      <ul class="benefits">
        <li class="benefits__lead">FREE ATM &amp; BTM (Bitcoin)<br>installation, maintenance, &amp; loading.</li>
        <li>Lower card processing fees</li>
        <li>Stimulate more traffic.</li>
        <li>Ease of access for customers</li>
        <li>Maintain customers inside location.</li>
        <li>Higher tips &amp; spending</li>
      </ul>
      <p class="contact-name">TOBIAS MERLANO</p>
      <div class="contact-icons">
        <svg class="contact-icon" viewBox="0 0 32 32" role="img" aria-label="Phone">
          <circle cx="16" cy="16" r="16" fill="var(--gold)"/>
          <path d="M11,8 L14,8 L15,12 L13,13.5 Q14.5,17.5 18.5,19 L20,17 L24,18 L24,21 Q24,24 21,24 Q9,23 8,11 Q8,8 11,8 Z" fill="var(--card-black)"/>
        </svg>
        <svg class="contact-icon" viewBox="0 0 32 32" role="img" aria-label="Email">
          <circle cx="16" cy="16" r="16" fill="var(--gold)"/>
          <rect x="8" y="10.5" width="16" height="11" fill="var(--card-black)"/>
          <path d="M8.5,11 L16,17 L23.5,11" fill="none" stroke="var(--gold)" stroke-width="1.4"/>
        </svg>
      </div>
      <p class="contact-phone">(512) 638-9071</p>
      <p class="contact-email">Tobias@KioskCoin.example</p>
    </div>
  </section>

</main>
</body>
</html>
```